Social Media Infographic for White Paper

Am working on a white paper on social media use by C-Suite Executives, and hope to include some infographics. I would like some help designing the first infographic.

The master bit of information is that "66% of C-Suite Executives use social media for professional purpose."

Within that 66%
-70% post original content on a daily/weekly basis
-13% of professional users are lurkers
-40% plan to use social media even more in the future

After initial design will need to two versions of the infographic, one listing the source at the bottom in small print (Source: 2017 Tollery Partners Executive Social Media Study), the other one with no source information.

Infographic design should be complimentary with my website: www.tollerypartners.example, but use of green should be very limited, if at all.

Target Market(s)

New media, C-Suite Executives, Executive Coaches

Industry/Entity Type

Management Consulting

Font styles to use
Sans Serif

Requirements
Must have
• Infographic with data displayed in a easy to understand format that tells the story of C-Suite Executives that participate in social media for professional purposes.
Nice to have
• Complements website design - www.tollery.example.
Should not have
• Limit use of green from website logo, which can be overpowering. Some is ok, but not too much

```html
<!DOCTYPE html>
<html lang="en">
<head>
<meta charset="utf-8">
<title>Social Media use by C-Suite Executives</title>
<link rel="stylesheet" href="https://fonts.googleapis.com/css2?family=Oswald:wght@400&family=Source+Sans+3:wght@400&display=swap">
<style>
  :root {
    --orange: #f9ae41;
    --orange-dark: #b5731e;
    --green: #39b14a;
    --ink: #231f20;
    --paper: #ffffff;
  }
  html, body {
    margin: 0;
    padding: 0;
    width: 1200px;
    height: 848px;
    overflow: hidden;
    background: var(--paper);
  }
  .infographic { display: block; width: 1200px; height: 848px; }
  .title {
    font-family: "Oswald", "Arial Narrow", sans-serif;
    font-size: 37px;
    fill: #000;
  }
  .rule { stroke: var(--orange); stroke-width: 3; }
  .slice-orange { fill: var(--orange); }
  .slice-green { fill: var(--green); }
  .slice-ink { fill: var(--ink); }
  .figure {
    font-family: "Source Sans 3", "Myriad Pro", sans-serif;
  }
  .figure-main { font-size: 42px; fill: #000; }
  .figure-light { font-size: 42px; fill: #fff; }
  .figure-small { font-size: 15px; fill: #fff; }
  .callout-box { fill: var(--orange); }
  .callout-fold { fill: var(--orange-dark); }
  .callout-text {
    font-family: "Source Sans 3", "Myriad Pro", sans-serif;
    font-size: 23px;
    fill: #000;
  }
  .arrow {
    stroke: var(--orange);
    stroke-width: 6;
    fill: none;
    stroke-linecap: butt;
    stroke-linejoin: miter;
  }
  .caption {
    font-family: "Source Sans 3", "Myriad Pro", sans-serif;
    font-size: 19px;
    fill: #000;
  }
</style>
</head>
<body>
<svg class="infographic" viewBox="0 0 1200 848" xmlns="http://www.w3.org/2000/svg" role="img" aria-label="Social Media use by C-Suite Executives">
  <!-- Heading -->
  <text class="title" x="30" y="60">Social Media use by C-Suite Executives</text>
  <line class="rule" x1="0" y1="74" x2="655" y2="74"/>
  <line class="rule" x1="0" y1="83" x2="655" y2="83"/>

  <!-- Master chart: 66% -->
  <g class="chart-master">
    <circle class="slice-green" cx="224" cy="400" r="184"/>
    <path class="slice-orange" d="M224 400 L137 237 A184 184 0 1 1 113 546 Z"/>
    <text class="figure figure-main" x="276" y="390">66%</text>
  </g>

  <!-- Callout -->
  <g class="callout">
    <path class="callout-fold" d="M407 330 L413 315 L413 330 Z"/>
    <path class="callout-box" d="M413 315 H610 V470 Q585 490 560 502 H413 Z"/>
    <text class="callout-text">
      <tspan x="420" y="355">66% of C-Suite</tspan>
      <tspan x="420" y="386">Executives use</tspan>
      <tspan x="420" y="417">social media for</tspan>
      <tspan x="420" y="448">professional</tspan>
      <tspan x="420" y="479">purpose.</tspan>
    </text>
  </g>

  <!-- Connecting arrows -->
  <g class="arrows">
    <path class="arrow" d="M600 292 L716 218"/>
    <path class="arrow" d="M686 211 L718 216 L704 246"/>
    <path class="arrow" d="M620 410 L714 410"/>
    <path class="arrow" d="M692 393 L714 410 L692 427"/>
    <path class="arrow" d="M600 515 L716 582"/>
    <path class="arrow" d="M704 553 L718 584 L686 588"/>
  </g>

  <!-- Sub chart: 70% -->
  <g class="chart-sub">
    <circle class="slice-green" cx="833" cy="158" r="108"/>
    <path class="slice-ink" d="M833 158 L783 62 A108 108 0 0 1 907 237 Z"/>
    <path class="slice-orange" d="M833 158 L907 237 A108 108 0 0 1 768 244 Z"/>
    <text class="figure figure-light" x="834" y="126">70%</text>
  </g>
  <text class="caption">
    <tspan x="957" y="98">70% post original</tspan>
    <tspan x="957" y="120">content on a</tspan>
    <tspan x="957" y="142">daily/weekly</tspan>
    <tspan x="957" y="164">basis</tspan>
  </text>

  <!-- Sub chart: 13% -->
  <g class="chart-sub">
    <circle class="slice-green" cx="833" cy="422" r="108"/>
    <path class="slice-orange" d="M833 422 L838 314 A108 108 0 1 1 768 508 Z"/>
    <path class="slice-ink" d="M833 422 L785 325 A108 108 0 0 1 838 314 Z"/>
    <text class="figure figure-small" x="795" y="342">13%</text>
  </g>
  <text class="caption">
    <tspan x="957" y="380">13% of professional</tspan>
    <tspan x="957" y="402">users are lurkers</tspan>
  </text>

  <!-- Sub chart: 40% -->
  <g class="chart-sub">
    <circle class="slice-green" cx="833" cy="665" r="108"/>
    <path class="slice-ink" d="M833 665 L782 570 A108 108 0 0 1 936 632 Z"/>
    <path class="slice-orange" d="M833 665 L936 632 A108 108 0 0 1 768 751 Z"/>
    <text class="figure figure-light" x="818" y="626">40%</text>
  </g>
  <text class="caption">
    <tspan x="950" y="646">40% plan to use social</tspan>
    <tspan x="950" y="668">media even more in</tspan>
    <tspan x="950" y="690">the future</tspan>
  </text>
</svg>
</body>
</html>
```